Business card design for new brand

We have recently rebranded and need a new business card template.

We are an insurance underwriting agency. All of our products are sold via other partner companies, so these are just to pass on our details to other organisations.

We would like to see designs that use the colour green (current stationary generally uses lime green (rgb 142,190,63) and forest green (0,154,79) to comply with our logo's colours. We are happy with other shades of green.

Business cards need to include our logo, as well as space for:
1. Full name
2. Qualifications (optional)
3. Title
4. Office number
5. Mobile number
6. Email address

Our logo is enclosed here.

```html
<!DOCTYPE html>
<html lang="en">
<head>
<meta charset="utf-8">
<title>Fernlea Australia – Business Card</title>
<link rel="stylesheet" href="https://fonts.googleapis.com/css2?family=Ubuntu:wght@400;500&family=Arimo:wght@400;700&display=swap">
<style>
  :root {
    --forest: #0f9347;
    --forest-deep: #0b7a3a;
    --lime: #8ebe3f;
    --ink: #222222;
    --muted: #444444;
    --paper: #ffffff;
    --canvas: #e9ebea;
  }
  * { box-sizing: border-box; margin: 0; padding: 0; }
  html, body { width: 1200px; height: 900px; overflow: hidden; }
  body {
    background: var(--canvas);
    display: flex;
    align-items: center;
    justify-content: center;
    gap: 40px;
    font-family: "Arimo", Arial, sans-serif;
  }
  .card {
    position: relative;
    width: 520px;
    height: 300px;
    border-radius: 22px;
    overflow: hidden;
    box-shadow: 0 6px 18px rgba(0,0,0,0.12);
  }

  /* Front */
  .card--front { background: var(--paper); color: var(--ink); }
  .brand {
    position: absolute;
    top: 34px;
    left: 38px;
    display: flex;
    align-items: flex-start;
    gap: 10px;
    font-family: "Ubuntu", sans-serif;
  }
  .brand__mark { width: 26px; height: 26px; background: var(--forest); margin-top: 4px; }
  .brand__name { font-size: 34px; font-weight: 400; line-height: 1; color: var(--ink); }
  .brand__sub { font-size: 15px; color: var(--muted); margin-top: 4px; padding-left: 4px; }

  .person {
    position: absolute;
    top: 118px;
    left: 38px;
    padding-left: 12px;
    border-left: 5px solid var(--forest);
  }
  .person__name { font-size: 21px; font-weight: 700; color: var(--lime); letter-spacing: 0.5px; }
  .person__title { font-size: 13px; color: var(--muted); margin-top: 3px; }

  .contact {
    position: absolute;
    top: 186px;
    left: 38px;
    list-style: none;
    font-size: 13px;
    color: var(--ink);
  }
  .contact li { display: flex; align-items: center; gap: 7px; margin-bottom: 5px; }
  .contact svg { width: 12px; height: 12px; fill: var(--forest); flex: none; }

  .accent-block {
    position: absolute;
    right: 48px;
    bottom: 48px;
    width: 150px;
    height: 150px;
    background: var(--forest);
  }

  /* Back */
  .card--back {
    background: var(--forest);
    color: var(--paper);
    display: flex;
    align-items: center;
    justify-content: center;
  }
  .back-brand { display: flex; align-items: flex-start; gap: 14px; font-family: "Ubuntu", sans-serif; }
  .back-brand__mark { width: 44px; height: 44px; background: var(--paper); margin-top: 8px; }
  .back-brand__name { font-size: 66px; font-weight: 500; line-height: 1; }
  .back-brand__sub { font-size: 27px; margin-top: 6px; padding-left: 6px; }
</style>
</head>
<body>

<section class="card card--front">
  <div class="brand">
    <span class="brand__mark"></span>
    <div>
      <div class="brand__name">Fernlea</div>
      <div class="brand__sub">Australia Pty Ltd</div>
    </div>
  </div>

  <div class="person">
    <div class="person__name">DANIEL HART</div>
    <div class="person__title">Director/Founder</div>
  </div>

  <ul class="contact">
    <li>
      <svg viewBox="0 0 24 24" aria-hidden="true"><path d="M6.6 10.8a15 15 0 0 0 6.6 6.6l2.2-2.2c.3-.3.7-.4 1-.2 1.1.4 2.3.6 3.6.6.6 0 1 .4 1 1V20c0 .6-.4 1-1 1A17 17 0 0 1 3 4c0-.6.4-1 1-1h3.5c.6 0 1 .4 1 1 0 1.3.2 2.5.6 3.6.1.3 0 .7-.2 1z"/></svg>
      123.555.0147
    </li>
    <li>
      <svg viewBox="0 0 24 24" aria-hidden="true"><path d="M7 1h10a2 2 0 0 1 2 2v18a2 2 0 0 1-2 2H7a2 2 0 0 1-2-2V3a2 2 0 0 1 2-2zm0 3v14h10V4zm5 15.5a1 1 0 1 0 0 2 1 1 0 0 0 0-2z"/></svg>
      123.555.0193
    </li>
    <li>
      <svg viewBox="0 0 24 24" aria-hidden="true"><path d="M2 5h20v14H2zm2 2v.5l8 5 8-5V7zm0 2.8V17h16V9.8l-8 5z"/></svg>
      info@fernleaaustralia.com
    </li>
    <li>
      <svg viewBox="0 0 24 24" aria-hidden="true"><path d="M12 2a10 10 0 1 0 0 20 10 10 0 0 0 0-20zm6.9 9h-3a15 15 0 0 0-1.3-5.5A8 8 0 0 1 18.9 11zM12 4c.9 1.2 1.8 3.6 1.9 7h-3.8c.1-3.4 1-5.8 1.9-7zM9.4 5.5A15 15 0 0 0 8.1 11h-3a8 8 0 0 1 4.3-5.5zM5.1 13h3a15 15 0 0 0 1.3 5.5A8 8 0 0 1 5.1 13zM12 20c-.9-1.2-1.8-3.6-1.9-7h3.8c-.1 3.4-1 5.8-1.9 7zm2.6-1.5a15 15 0 0 0 1.3-5.5h3a8 8 0 0 1-4.3 5.5z"/></svg>
      www.fernleaaustralia.com
    </li>
  </ul>

  <div class="accent-block"></div>
</section>

<section class="card card--back">
  <div class="back-brand">
    <span class="back-brand__mark"></span>
    <div>
      <div class="back-brand__name">Fernlea</div>
      <div class="back-brand__sub">Australia Pty Ltd</div>
    </div>
  </div>
</section>

</body>
</html>
```